Hollowmere Farm Promotional Leaflet

The team at Hollowmere Farm can help with every aspect of managing and enhancing your home from housekeeping and professional cleaning, laundry and ironing to providing chic and contemporary flower arrangements and even food for your pets!We take pride in providing high-end, consistent and reliable professional services bespoke to you. Whether you are a busy professional working long hours, a stay-at home parent or retired; having professional help in the home gives you time to spend on the things you enjoy.We are providing a very upmarket, highly professional service and need an A5 promotional leaflet to be designed. Please refer to www.hollowmerefarm-example.co.uk and see the section on 'Home Management'The leaflet should incorporate the Hollowmere Farm logo without the 'tipi', and any suitable photography images used on the home page of the website or the 'home management' section.

Target Market(s)

high-end, affluent owners of luxury homes

Industry/Entity Type

Farm

Contact Information for Business Card

The business card design needs to be suitable for use across all of Hollowmere Farm businesses, specifically:
Hollowmere Farm Home Management - otherwise known as Hollowmere Farm @ Home (this uses the typographical logo
Hollowmere Farm Weddings & Events - this uses the 'tipi' logo

Requirements
Must have
• Design in keeping with the look and feel of the logo and website design
• www.hollowmerefarm-example.co.uk

```html
<!DOCTYPE html>
<html lang="en">
<head>
<meta charset="utf-8">
<title>Hollowmere Farm Home Management</title>
<link rel="stylesheet" href="https://fonts.googleapis.com/css2?family=Catamaran:wght@400;500;600;700;800&display=swap">
<style>
  :root {
    --brand-pink: #d81b5c;
    --heading-pink: #c8195a;
    --ink: #2a2a2a;
    --white: #ffffff;
    --frame: #5e5e5e;
    --mist: #e6e6e6;
    --night: #1f2d6b;
  }
  * { margin: 0; padding: 0; box-sizing: border-box; }
  html, body { width: 839px; height: 1200px; overflow: hidden; background: var(--white); }
  body { font-family: "Catamaran", sans-serif; color: var(--ink); }
  .leaflet { position: relative; width: 839px; height: 1200px; overflow: hidden;
    background: linear-gradient(90deg, var(--mist) 0%, #f6f6f6 35%, var(--white) 60%); }

  .hero-photo { position: absolute; left: 0; top: 0; width: 839px; height: 336px;
    background: radial-gradient(ellipse at 50% 85%, #d9a85a 0%, #7a5a3a 22%, #2b3f86 50%, var(--night) 100%); }

  .title-band { position: absolute; left: 0; top: 336px; width: 839px; height: 140px; }
  .title-band svg { position: absolute; inset: 0; }
  .title-band h1 { position: absolute; top: 10px; width: 100%; text-align: center; color: var(--white);
    font-weight: 700; font-size: 41px; letter-spacing: -0.3px; line-height: 48px; }
  .title-band .intro { position: absolute; top: 60px; width: 100%; text-align: center; color: var(--white);
    font-weight: 600; font-size: 17px; line-height: 22px; }

  .section-heading { position: absolute; left: 50px; color: var(--heading-pink);
    font-weight: 600; font-size: 22.5px; line-height: 28px; }
  .service-list { position: absolute; left: 50px; list-style: none; font-size: 19.5px; line-height: 24.3px; font-weight: 500; }
  .service-list li { position: relative; padding-left: 23px; }
  .service-list li::before { content: ""; position: absolute; left: 1px; top: 7px; width: 11px; height: 11px;
    border-radius: 50%; background: var(--brand-pink); }

  .photo-frame { position: absolute; border-radius: 9px; border: 4px solid var(--frame);
    box-shadow: 2px 3px 0 #3c3c3c; }
  .photo-table { left: 537px; top: 545px; width: 281px; height: 147px;
    background: radial-gradient(circle at 65% 55%, #f4c9b8 0%, #e0603a 30%, #b61c40 65%, #6a0f2a 100%); }
  .photo-tipis { left: 570px; top: 709px; width: 248px; height: 127px;
    background: linear-gradient(180deg, #7c9a5c 0%, #d8c8a8 40%, #c9b58f 75%, #8c9a66 100%); }
  .photo-canapes { left: 537px; top: 856px; width: 281px; height: 147px;
    background: radial-gradient(ellipse at 50% 55%, #f2a23a 0%, #e8d6b4 40%, #cfd6c2 75%, #9aa58a 100%); }

  .pride-band { position: absolute; left: 0; top: 711px; width: 580px; height: 125px; background: var(--brand-pink);
    color: var(--white); font-size: 19.5px; font-weight: 500; line-height: 24px; padding: 11px 0 0 50px; }
  .pride-band p + p { margin-top: 5px; }

  .coverage-pill { position: absolute; left: 204px; top: 1019px; width: 660px; height: 36px;
    background: var(--brand-pink); border-radius: 18px 0 0 18px; color: var(--white);
    font-style: italic; font-weight: 600; font-size: 18.5px; line-height: 36px; padding-left: 22px; }

  .contact-footer { position: absolute; left: 0; top: 1067px; width: 839px; height: 133px; background: var(--brand-pink);
    color: var(--white); }
  .contact-details { position: absolute; left: 50px; top: 14px; font-weight: 700; font-size: 18px; line-height: 24.5px; }
  .brand-name { position: absolute; left: 520px; top: 46px; width: 290px; text-align: center;
    color: #f3b8cd; font-weight: 500; font-size: 30px; line-height: 36px; }
</style>
</head>
<body>
<main class="leaflet">
  <div class="hero-photo" role="img" aria-label="Photograph of illuminated tipi marquees at dusk hosting an evening reception with fairy lights and bunting"></div>

  <header class="title-band">
    <svg width="839" height="140" viewBox="0 0 839 140" aria-hidden="true">
      <path d="M0 70 L0 0 L839 0 L839 70 Q420 180 0 70 Z" fill="#9a9a9a"/>
      <path d="M0 72 L0 0 L839 0 L839 72 Q420 166 0 72 Z" fill="var(--white)"/>
      <path d="M0 70 L0 0 L839 0 L839 70 Q420 160 0 70 Z" fill="var(--brand-pink)"/>
    </svg>
    <h1>Hollowmere Farm Home Management</h1>
    <p class="intro">The Team @ Hollowmere Farm Can Help With Every Aspect Of Managing<br>And Enhancing Your Home Including:</p>
  </header>

  <h2 class="section-heading" style="top:491px">Regular housekeeping and professional cleaning</h2>
  <ul class="service-list" style="top:523px">
    <li>Exit cleans</li>
    <li>One-off seasonal /party / building work cleans</li>
    <li>Laundry and ironing</li>
    <li>Chic and contemporary flower arrangements</li>
    <li>Car valeting</li>
    <li>Pet food delivery</li>
    <li>Dry cleaning</li>
  </ul>

  <div class="photo-frame photo-table" role="img" aria-label="Photograph of a candlelit dining table with a pink rose centrepiece"></div>

  <section class="pride-band">
    <p>We take pride in providing high-end, consistent and<br>reliable professional services bespoke to you.</p>
    <p>Coming home to a beautiful environment and being able<br>to relax and enjoy your time is something we all deserve.</p>
  </section>
  <div class="photo-frame photo-tipis" role="img" aria-label="Photograph of canvas tipis decorated with greenery on a lawn"></div>

  <h2 class="section-heading" style="top:847px">Satisfaction guaranteed</h2>
  <ul class="service-list" style="top:876px">
    <li>Professional staff you can trust and rely on</li>
    <li>Competitive rates</li>
    <li>CRB checked and referenced</li>
    <li>Member of the Domestic Staffing Guild<br>Federation</li>
    <li>Fully Insure</li>
  </ul>
  <div class="photo-frame photo-canapes" role="img" aria-label="Photograph of a platter of colourful canapés on skewers"></div>

  <p class="coverage-pill">We look after our clients’ homes and holiday lets across South Somerset.</p>

  <footer class="contact-footer">
    <div class="contact-details">
      <p>Contact Us To Arrange A Home Visit And Quotation:</p>
      <p>E: info@hollowmerefarm-example.co.uk</p>
      <p>T: 07700900418</p>
      <p>www.hollowmerefarm-example.co.uk</p>
    </div>
    <p class="brand-name">Hollowmere Farm</p>
  </footer>
</main>
</body>
</html>
```